Steel Rebar Fabrication Company needs Facebook Ads & page, Instagram Ads & pages designed.

I want to put out an Instagram, Facebook ad, and LinkedIn campaign out for my new company, Ridgeform Metals Inc. I want the ads to be short but clean, clear and precise. I want our address: 4817 Alderbrook Cres. Tsawwassen, BC. I want our hours of operation to be listed 8:00am to 4:00pm Monday to Friday. Product Delivery to your job site or pick up at our yard available. We can cut, bend to custom and standard shapes based upon Canadian NRQ Standards. We offer products ranging from 10mm to 35mm diameter Grade 400W rebar. We can bend stirrups, dowels, hairpins; whatever your company needs to complete your product. Whether it is a small project, Tilt Up warehouse, Wood Frame Construction with Concrete parkade foundation; we have the team to meet your needs.
Email address: info@ridgeformmetalsinc.ca
We can service all areas of British Columbia.

Target Market(s)

Construction Company's for homes, condominiums, warehouses, commercial, industrial, and infrastructure projects. As well, as the every day DIY home improvement or renovator.

Industry/Entity Type

Construction

Requirements
Nice to have
• Would like to see a image of the rebar steel that I have provided in the ad. Even if it is in the background with a lower opacity level. Bonus if someone includes any of the movie files I have uploaded.

```html
<!DOCTYPE html>
<html lang="en">
<head>
<meta charset="utf-8">
<title>Ridgeform Metals Inc. – Grade 400W Rebar</title>
<link rel="stylesheet" href="https://fonts.googleapis.com/css2?family=Jost:ital,wght@0,400;0,500;0,600;1,400&display=swap">
<style>
  :root {
    --red-top: #e58a8e;
    --red-mid: #cf3440;
    --red-deep: #b81c2a;
    --brand-red: #c8202e;
    --ink: #1f1f1f;
    --white: #ffffff;
    --rust-1: #8a5a3a;
    --rust-2: #c9a67c;
    --rust-3: #5e3a24;
  }
  * { margin: 0; padding: 0; box-sizing: border-box; }
  html, body { width: 1200px; height: 1198px; overflow: hidden; background: var(--white); }
  .ad {
    position: relative;
    width: 1200px;
    height: 1198px;
    font-family: "Jost", "Futura", sans-serif;
    overflow: hidden;
  }
  .hero {
    position: absolute;
    left: 0; top: 0;
    width: 1200px; height: 886px;
    background: linear-gradient(170deg, var(--red-top) 0%, var(--red-mid) 45%, var(--red-deep) 100%);
  }
  .hero-photo {
    position: absolute;
    left: 0; top: 0;
    width: 1200px; height: 886px;
  }
  .headline {
    position: absolute;
    left: 96px; top: 160px;
    color: var(--white);
    font-style: italic;
    font-weight: 400;
    font-size: 74px;
    line-height: 115px;
    letter-spacing: 1.5px;
  }
  .service-info {
    position: absolute;
    left: 46px; top: 750px;
    color: var(--white);
    font-style: italic;
    font-size: 30px;
    line-height: 50px;
  }
  .brand {
    position: absolute;
    left: 0; top: 920px;
    width: 1200px;
    text-align: center;
    color: var(--ink);
    font-weight: 600;
    font-size: 64px;
    letter-spacing: 1px;
  }
  .address {
    position: absolute;
    left: 0; top: 1072px;
    width: 1200px;
    text-align: center;
    color: var(--ink);
    font-size: 30px;
    letter-spacing: 3px;
  }
  .email-bar {
    position: absolute;
    left: 0; top: 1138px;
    width: 1200px; height: 60px;
    background: var(--brand-red);
    color: var(--white);
    font-size: 30px;
    letter-spacing: 3px;
    text-align: center;
    line-height: 60px;
  }
</style>
</head>
<body>
<main class="ad">
  <section class="hero">
    <svg class="hero-photo" viewBox="0 0 1200 886" role="img" aria-label="Photograph of rusty rebar mesh and bent rebar cages">
      <defs>
        <linearGradient id="rebarTone" x1="0" y1="0" x2="1" y2="1">
          <stop offset="0" stop-color="var(--rust-2)"/>
          <stop offset="0.5" stop-color="var(--rust-1)"/>
          <stop offset="1" stop-color="var(--rust-3)"/>
        </linearGradient>
      </defs>
      <polygon points="826,0 1200,0 1200,886 1006,886" fill="url(#rebarTone)"/>
    </svg>
    <h1 class="headline">We Offer Products<br>Ranging from 10mm<br>to 35mm Diameter<br>Grade 400w Rebar</h1>
    <p class="service-info">We can service all areas of British Columbia.<br>Our Timings: Monday to Friday 8:00am to 4:00pm</p>
  </section>
  <p class="brand">Ridgeform Metals Inc.</p>
  <p class="address">4817 Alderbrook Cres. Tsawwassen, BC.</p>
  <p class="email-bar">Email address: info@ridgeformmetalsinc.ca</p>
</main>
</body>
</html>
```